Inspiring Poster for Company Staff Room

What we need:
We want an awesome design to create a poster that will be plaque mounted in our staff room. We just went through a very motivating workshop to discover our "WHY" as a company...basically, to define the reason we are in business, and to define what motivates us to come to work every day. The poster must be motivating but really resonate with our team…we are not looking for a “typical” motivational poster that we can purchase off Amazon!

Who we are:
We are a property management company, a team of 20 that is passionate about our investors, and residents who rent from us, but more importantly, we love helping people and making a difference in our industry. We are proud and work hard for every single 5 star Google review we achieve.

Information for you:
We have included a mock up of the poster, which words we want, and the placement of them (in a general sense) but we need a designer to really bring this together in an inspiring poster that represents our company’s culture, feel, and fit. We have also included a logo file, as well as examples of our business cards, letterhead and thank you card already designed.
Here are the parameters:

(1) Poster size: 24” x 36”
(2) Full colour
(3) Must incorporate our company logo
(4) Must incorporate the following words:

Why do I come to work?

“To feel fulfilled by empathizing, educating and empowering our clients and co-workers so that we can build strong, impactful relationships”

Own the outcome

(5) Please see our website at www.brindlecovepm.com to get a feel for our company culture and for a better idea of our current company graphics

Target Market(s)

Our staff. Will not be seen by our clients

Industry/Entity Type

Real Estate

Font styles to use
Serif
Sans Serif

Requirements
Should not have
• Would not want this to be too "busy." if you can picture it, the poster will be mounted on the wall as soon as someone enters the room. The idea is to remind them each day why they come to work.

```html
<!DOCTYPE html>
<html lang="en">
<head>
<meta charset="utf-8">
<title>Why Do I Come To Work – Staff Room Poster</title>
<link rel="stylesheet" href="https://fonts.googleapis.com/css2?family=Montserrat:wght@500;600;700;800&display=swap">
<style>
  :root {
    --page-bg: #dcdcdc;
    --slate-top: #62605d;
    --slate-mid: #3d3b38;
    --slate-bottom: #1b1915;
    --orange: #f28a1a;
    --rust: #a85a5a;
    --body-orange: #ec9436;
    --peach: #f2c18e;
    --white: #ffffff;
  }
  * { margin: 0; padding: 0; box-sizing: border-box; }
  html, body {
    width: 1200px; height: 1200px; overflow: hidden;
    background: var(--page-bg);
    font-family: "Montserrat", sans-serif;
  }
  .poster {
    position: absolute;
    left: 226px; top: 40px;
    width: 747px; height: 1120px;
    background:
      radial-gradient(ellipse at 55% 20%, rgba(255,255,255,0.08), transparent 60%),
      linear-gradient(180deg, var(--slate-top) 0%, var(--slate-mid) 45%, var(--slate-bottom) 100%);
    overflow: hidden;
  }
  .brand {
    position: absolute;
    left: 500px; top: 38px;
    display: flex; align-items: center; gap: 8px;
    color: var(--white);
    font-weight: 600;
    text-transform: uppercase;
  }
  .brand-mark { width: 20px; height: 20px; background: var(--white); }
  .brand-name { font-size: 12px; line-height: 14px; letter-spacing: 0.5px; }
  .brand-name span { display: block; font-size: 7.5px; line-height: 10px; letter-spacing: 1.2px; }
  .headline-art { position: absolute; left: 0; top: 0; }
  .question {
    position: absolute;
    left: 294px; top: 170px;
    font-weight: 800;
    font-size: 70px;
    line-height: 56px;
    letter-spacing: -2px;
    text-transform: uppercase;
    background: linear-gradient(180deg, var(--body-orange), var(--rust));
    -webkit-background-clip: text; background-clip: text;
    color: transparent;
    filter: drop-shadow(2px 2px 2px rgba(0,0,0,0.45));
  }
  .why-statement {
    position: absolute;
    left: 131px; top: 618px;
    width: 520px;
    font-weight: 500;
    font-size: 38px;
    line-height: 40.5px;
    letter-spacing: -0.6px;
    color: var(--body-orange);
  }
  .motto {
    position: absolute;
    left: 131px; top: 950px;
    font-weight: 700;
    font-size: 37px;
    letter-spacing: -0.8px;
    color: var(--peach);
  }
</style>
</head>
<body>
  <main class="poster">
    <div class="brand">
      <div class="brand-mark"></div>
      <div class="brand-name">Brindle Cove<span>Property Management</span></div>
    </div>

    <svg class="headline-art" width="747" height="1120" viewBox="0 0 747 1120" aria-label="Why?">
      <defs>
        <linearGradient id="why-gradient" x1="0" y1="0" x2="0.5" y2="1">
          <stop offset="0" stop-color="var(--orange)"/>
          <stop offset="1" stop-color="var(--rust)"/>
        </linearGradient>
        <filter id="soft-shadow" x="-10%" y="-10%" width="130%" height="130%">
          <feDropShadow dx="3" dy="3" stdDeviation="2" flood-color="#000" flood-opacity="0.45"/>
        </filter>
      </defs>
      <text class="why-word" transform="translate(268,600) rotate(-90)"
            font-family="Montserrat, sans-serif" font-weight="800" font-size="192"
            textLength="478" lengthAdjust="spacingAndGlyphs"
            fill="url(#why-gradient)" filter="url(#soft-shadow)">WHY</text>
      <text class="question-mark" x="286" y="586"
            font-family="Montserrat, sans-serif" font-weight="800" font-size="236"
            fill="url(#why-gradient)" filter="url(#soft-shadow)">?</text>
    </svg>

    <h1 class="question">Do I<br>Come<br>To<br>Work</h1>

    <p class="why-statement">To feel fulfilled by empathizing, educating and empowering our clients and co-workers so that we can build strong, impactful relationships.</p>

    <p class="motto">Own the outcome.</p>
  </main>
</body>
</html>
```